Web Design for Meadowfield Turf Crew

Meadowfield Turf Crew needs the photoshop files for a simple, clean and professional web design. I need a home and subpage design, although they can be very similar. See pagestridehub.com for a desired layout, although I'd like to see more design than shown on that site. The goal of the site is to attract both lawn maintenance/landscape customers and build a partner network of consultants that serve the US market. The following are needed:

- home and subpage design
- page: Home, Services, Locations, Consultants, FAQ, Contact
- if subpages have header photo, need to include 5 different header photos for each page
- favicon
Updates

I'll award the design based on the homepage concept. The minor subpage changes and other elements can be worked out in the workroom stage. Thanks, Trent

Industry/Entity Type

It Professional

```html
<!DOCTYPE html>
<html lang="en">
<head>
<meta charset="utf-8">
<title>Meadowfield Turf Crew</title>
<link rel="stylesheet" href="https://fonts.googleapis.com/css2?family=Open+Sans:wght@300;400;600&family=Arimo:wght@400&display=swap">
<style>
:root{
  --page-bg:#ffffff;
  --header-bg:#f7f7f7;
  --rule:#c9c9c9;
  --brand-grey:#5b5b5b;
  --brand-green:#6cb33e;
  --text-dark:#333333;
  --nav-text:#3e3e3e;
  --footer-text:#555555;
  --submit:#f04a23;
  --frame:#555555;
}
*{margin:0;padding:0;box-sizing:border-box}
html,body{width:1200px;height:1200px;overflow:hidden;background:var(--page-bg)}
body{position:relative;font-family:"Open Sans",Arial,sans-serif;color:var(--text-dark)}

.site-header{position:absolute;left:0;top:0;width:1200px;height:156px;background:var(--header-bg);border-bottom:1px solid var(--rule)}
.brand{position:absolute;left:44px;top:40px;height:70px;display:flex;align-items:center;gap:16px}
.brand-mark{width:36px;height:36px;background:var(--brand-green);border-radius:4px}
.brand-name{font-family:"Open Sans",Arial,sans-serif;font-weight:400;font-size:36px;color:var(--brand-grey);letter-spacing:0.5px}

.phone{position:absolute;right:48px;top:19px;display:flex;align-items:center;gap:10px}
.phone-icon{width:51px;height:44px;border:1px solid #9a9a9a;border-radius:4px;background:#ececec;display:flex;align-items:center;justify-content:center}
.phone-number{font-size:29px;font-weight:600;color:var(--brand-grey);letter-spacing:1px}

.main-nav{position:absolute;right:48px;top:106px;display:flex;height:36px;align-items:center}
.main-nav a{font-size:15px;font-weight:600;color:var(--nav-text);text-decoration:none;text-transform:uppercase;padding:0 15px;line-height:36px}
.main-nav a.is-active{background:var(--brand-green);color:#fff;border-radius:2px;padding:0 20px;margin-right:-4px}
.main-nav a:last-child{padding-right:0}

.hero{position:absolute;left:44px;top:178px;width:1112px;height:502px;border:2px solid var(--frame);
  background:linear-gradient(180deg,#5e6e4a 0%,#3f7a2a 22%,#c2428a 30%,#7bbf2e 40%,#8ccb33 70%,#79b82a 100%)}

.welcome{position:absolute;left:44px;top:712px;width:700px}
.welcome h1{font-weight:300;font-size:27px;color:#4a4a4a;margin-bottom:14px;letter-spacing:-0.2px}
.welcome p{font-family:"Arimo",Arial,sans-serif;font-size:14.4px;line-height:24px;text-align:justify;letter-spacing:0.6px;color:#2e2e2e}

.contact-card{position:absolute;left:780px;top:726px;width:371px;height:360px;background:var(--brand-green);border-radius:5px;color:#fff}
.contact-card h2{font-family:"Arimo",Arial,sans-serif;font-weight:400;font-size:22px;text-align:center;margin-top:20px;letter-spacing:1px;padding-left:26px}
.field{position:absolute;left:18px;width:336px;display:flex;align-items:center;justify-content:space-between}
.field label{font-family:"Arimo",Arial,sans-serif;font-size:16px;letter-spacing:1px}
.field span.input{width:226px;height:29px;background:#fff;border-radius:3px;display:block}
.field-name{top:76px}.field-email{top:133px}.field-phone{top:190px}
.submit{position:absolute;left:100px;top:258px;width:196px;height:44px;background:var(--submit);color:#fff;border:none;font-family:"Arimo",Arial,sans-serif;font-size:21px;letter-spacing:0.5px}

.site-footer{position:absolute;left:0;top:1133px;width:1200px;border-top:1px solid var(--rule);height:67px}
.footer-nav{position:absolute;left:44px;top:12px;display:flex;gap:27px}
.footer-nav a{font-size:13px;color:var(--footer-text);text-decoration:none;letter-spacing:0.5px}
.copyright{position:absolute;right:52px;top:12px;font-family:"Arimo",Arial,sans-serif;font-size:13px;color:#444;letter-spacing:0.6px}
</style>
</head>
<body>
<header class="site-header">
  <div class="brand">
    <span class="brand-mark"></span>
    <span class="brand-name">Meadowfield Turf Crew</span>
  </div>
  <div class="phone">
    <span class="phone-icon">
      <svg width="30" height="26" viewBox="0 0 30 26"><path d="M3 9c0-4 5-6 12-6s12 2 12 6v2h-6V8H9v3H3z" fill="#555"/><rect x="6" y="12" width="18" height="11" rx="2" fill="#555"/><circle cx="15" cy="17" r="3" fill="#ececec"/></svg>
    </span>
    <span class="phone-number">910 555 0148</span>
  </div>
  <nav class="main-nav">
    <a class="is-active" href="#">Home</a>
    <a href="#">Services</a>
    <a href="#">Locations</a>
    <a href="#">Consultants</a>
    <a href="#">FAQ</a>
    <a href="#">Contact</a>
  </nav>
</header>

<div class="hero" role="img" aria-label="Photo of a manicured green lawn with flower beds and shrubs in front of a house porch"></div>

<section class="welcome">
  <h1>Welcome to Meadowfield Turf Crew</h1>
  <p>Lorem ipsum dolor sit amet, consectetur adipiscing elit. Pellentesque blandit mauris nec consectetur luctus. Proin ornare mauris sit amet enim tincidunt, vitae sollicitudin orci convallis. Donec eu tellus eros. Fusce pellentesque metus ac neque venenatis, non scelerisque neque condimentum. Cras et faucibus lorem. Suspendisse pulvinar neque non sem molestie eleifend. Nam vestibulum in mauris sed bibendum. Morbi sed egestas orci. Integer elementum, metus condimentum varius rhoncus, lectus augue egestas massa, at porta nulla est ac tortor. Morbi lacinia sagittis ante, sed posuere massa condimentum a. Sed feugiat lorem in fermentum placerat. Nulla in metus interdum eros vulputate porta. Mauris risus erat, cursus eget egestas porta, lobortis a enim.</p>
</section>

<aside class="contact-card">
  <h2>CONTACT US</h2>
  <div class="field field-name"><label>Name</label><span class="input"></span></div>
  <div class="field field-email"><label>email</label><span class="input"></span></div>
  <div class="field field-phone"><label>Phone no.</label><span class="input"></span></div>
  <button class="submit">Submit</button>
</aside>

<footer class="site-footer">
  <nav class="footer-nav">
    <a href="#">Home</a><a href="#">Services</a><a href="#">Locations</a><a href="#">Consultants</a><a href="#">FAQ</a><a href="#">Contact</a>
  </nav>
  <div class="copyright">Copyright 2014 Meadowfield Turf Crew</div>
</footer>
</body>
</html>
```